I need the below text put into an illustration/high res image so I can print out and frame and give to my fiance. Can be simple but must look elegant. Idea is that the text can be written in the sand on the attached pics (let me know if you require more high res). Not precious on the dimensions but think no more than 90cm length or width. Can be smaller whatever you think works best. You can half long sentences if you think it will look better.
Update: some of you asked for a picture of us, not sure it works but have attached one
Marriage
Marriage isn’t for you.
You don’t marry to make yourself happy, you marry to make someone else happy.
More than that, your marriage isn’t for yourself, you’re marrying for a family.
Not just for the in-laws and all of that nonsense, but for your future children.
Who do you want to help you raise them?
Who do you want to influence them?
Marriage isn’t for you.
It’s not about you.
Marriage is about the person you married.

```html
<!DOCTYPE html>
<html lang="en">
<head>
<meta charset="utf-8">
<title>Marriage</title>
<link rel="stylesheet" href="https://fonts.googleapis.com/css2?family=Great+Vibes&display=swap">
<style>
  :root {
    --ink: #1c4a3a;
    --sky: #eef3f4;
    --sea-light: #cfe0e6;
    --sea: #a9c4cf;
    --wet-sand: #c9cfcf;
    --sand: #d9d7d0;
    --sand-deep: #d2cfc6;
  }
  html, body {
    margin: 0;
    padding: 0;
    width: 765px;
    height: 1200px;
    overflow: hidden;
    background: var(--sand);
  }
  .poster {
    display: block;
    width: 765px;
    height: 1200px;
  }
  .poster-title {
    font-family: "Great Vibes", cursive;
    font-size: 56px;
    font-weight: 700;
    fill: var(--ink);
    stroke: var(--ink);
    stroke-width: 0.6px;
  }
  .verse-line {
    font-family: "Great Vibes", cursive;
    font-size: 33px;
    fill: var(--ink);
  }
</style>
</head>
<body>
<svg class="poster" viewBox="0 0 765 1200" xmlns="http://www.w3.org/2000/svg">
  <defs>
    <linearGradient id="beach-tones" x1="0" y1="0" x2="0" y2="1">
      <stop offset="0" stop-color="var(--sky)"/>
      <stop offset="0.05" stop-color="var(--sea-light)"/>
      <stop offset="0.1" stop-color="var(--sea)"/>
      <stop offset="0.2" stop-color="var(--wet-sand)"/>
      <stop offset="0.45" stop-color="var(--sand)"/>
      <stop offset="1" stop-color="var(--sand-deep)"/>
    </linearGradient>
  </defs>

  <rect class="beach-photo" x="0" y="0" width="765" height="1200" fill="url(#beach-tones)"
        role="img" aria-label="Photograph of a calm beach with waves, distant hills and a single white rose lying on the sand"/>

  <text class="poster-title" x="34" y="84">Marriage</text>

  <g class="verse">
    <text class="verse-line" x="48" y="187">Marriage isn’t for you.</text>

    <text class="verse-line" x="50" y="296">You don’t marry to make yourself happy,</text>
    <text class="verse-line" x="32" y="353">you marry to make someone else happy.</text>

    <text class="verse-line" x="48" y="451">More than that, your marriage isn’t for</text>
    <text class="verse-line" x="32" y="511">yourself, you’re marrying for a family.</text>

    <text class="verse-line" x="48" y="609">Not just for the in-laws and all of that non-</text>
    <text class="verse-line" x="43" y="663">sense, but for your future children.</text>

    <text class="verse-line" x="53" y="765">Who do you want to help you raise them?</text>
    <text class="verse-line" x="53" y="820">Who do you want to influence them?</text>

    <text class="verse-line" x="48" y="923">Marriage isn’t for you.</text>
    <text class="verse-line" x="43" y="983">It’s not about you.</text>

    <text class="verse-line" x="48" y="1136">Marriage is about the person you married.</text>
  </g>
</svg>
</body>
</html>
```